Following list to be designed:

1. A4 Letter Head

Must comprise of:
BRISK HARBOR and its LOGO
Address: No.41, 2F, Telvin Court, Marlow Lane, Upper Fennel Gardens, Bangalore 560 078
Tel: 080 41927380
Fax: 080 41927381
Mail: hello@briskharbor.example

Color of wordings to be in the lighter shade of blue and brighter shade of blue.

2. A4 Envelope

Must comprise of:
BRISK HARBOR and its LOGO
Tel: 080 41927380
Fax: 080 41927381

3. Postal Envelope

Must comprise of:
BRISK HARBOR and its LOGO
Tel: 080 41927380
Fax: 080 41927381

4. Business Card

Must comprise of:
Ravi Menon
Managing Partner
Cell: +91 9847162053
Mail: ravimenon@briskharbor.example
Tel: 080 41927380
Fax: 080 41927381

5. A4 Letter Head

Must comprise of:
BRISK HARBOR CORP. (wording) and BRISK HARBOR LOGO (only blue ribbon)

Blue ribbon (BRISK HARBOR LOGO) may be placed on Left Top Corner of the A4 Letter Head
and BRISK HARBOR CORP. (wording) to be placed on Right Top Corner of the A4 Letter Head

Tel: 080 41927380
Fax: 080 41927381

6. . A4 Envelope

Must comprise of:

Blue ribbon (BRISK HARBOR LOGO) may be placed on Left Top Corner of the A4 Envelope
and BRISK HARBOR CORP. (wording) to be placed on Right Top Corner of the A4 Envelope
Tel: 080 41927380
Fax: 080 41927381

Target Market(s)

Top IT/ITES Organizations

Industry/Entity Type

Real Estate Development

Font styles to use
Serif
Sans Serif

Colors
33a6d7
0792cd
85cae6

Requirements
Should not have
• Playful font and color

```html
<!DOCTYPE html>
<html lang="en">
<head>
<meta charset="utf-8">
<title>Brisk Harbor – Envelope Back</title>
<link rel="stylesheet" href="https://fonts.googleapis.com/css2?family=Noto+Sans:wght@400;600&display=swap">
<style>
  :root {
    --paper: #ffffff;
    --brand-blue: #33a6d7;
    --contact-blue: #0b93cf;
    --name-grey: #66665f;
  }
  * { margin: 0; padding: 0; box-sizing: border-box; }
  html, body {
    width: 1200px;
    height: 848px;
    overflow: hidden;
    background: var(--paper);
  }
  .envelope {
    position: relative;
    width: 1200px;
    height: 848px;
    background: var(--paper);
    font-family: "Noto Sans", Verdana, sans-serif;
  }
  .brand {
    position: absolute;
    left: 102px;
    top: 482px;
    width: 240px;
  }
  .brand-mark {
    display: block;
    margin-left: 88px;
    width: 60px;
    height: 60px;
  }
  .brand-name {
    margin-top: 22px;
    font-size: 27px;
    font-weight: 600;
    letter-spacing: 0.5px;
    color: var(--name-grey);
    line-height: 1;
    white-space: nowrap;
  }
  .contact {
    position: absolute;
    left: 102px;
    top: 625px;
    font-size: 19.5px;
    line-height: 24px;
    letter-spacing: 0.4px;
    color: var(--contact-blue);
    list-style: none;
  }
</style>
</head>
<body>
  <main class="envelope">
    <div class="brand">
      <svg class="brand-mark" viewBox="0 0 60 60" aria-hidden="true">
        <circle cx="30" cy="30" r="30" fill="var(--brand-blue)"/>
      </svg>
      <div class="brand-name">BRISK HARBOR</div>
    </div>
    <ul class="contact">
      <li>No.41, 2F, Telvin Court, Marlow Lane</li>
      <li>Upper Fennel Gardens, Bangalore 560 078</li>
      <li>Tel: 080 41927380</li>
      <li>Fax: 080 41927381</li>
      <li>Mail: hello@briskharbor.example</li>
    </ul>
  </main>
</body>
</html>
```